Web Design Project

Full website, similar _function_ to http://www.kindmarrow.com/
You can not only make charities, but also communicate social or environmental problems by posting them on the website.
I need a full layout design, right now I am using a slightly changed bootstrap. View attached file "basic css" for current containers layout
Including front page, static text page (SEO), show listing page and content page, all the same look and feel. Dont focus to hard on the charity part...

Logo will be needed:
The URL - also the Logo - is Wehklang.de - that is German for "Outcry" - so working with a "!" makes prob. sense, like Wehklang!de or so... (EXTRA)

Colour Scheme:
I do not have a colour scheme, but I alreay think "Red URL with green elements" would be nice - that means please give me some other ideas ... I am not a designer, right?! :)

NO CODING NEEDED
Updates

Project Deadline Extended
Reason: I just got too few designs, some nice with it, though - I will clarify my needs new so it will be easier to reply with suggestions! :)

Target Market(s)

People who want to do charity and help other people

Industry/Entity Type

Charity

Requirements
Must have
• responsive design (tablet, smartphone)
static frame header (like here at pixelforum)

```html
<!DOCTYPE html>
<html lang="en">
<head>
<meta charset="utf-8">
<title>Wehklang!de – Charity</title>
<link rel="stylesheet" href="https://fonts.googleapis.com/css2?family=Source+Sans+3:wght@400;600&display=swap">
<style>
:root{
  --green-dark:#0a7a2c;
  --green:#13963a;
  --green-light:#1fa447;
  --green-text:#14902f;
  --bg:#f3f3f3;
  --panel:#ffffff;
  --line:#d6d6d6;
  --text:#555555;
  --text-dark:#333333;
  --nav-text:#ffffff;
}
*{box-sizing:border-box;margin:0;padding:0}
html,body{width:1120px;height:1200px;overflow:hidden}
body{background:var(--bg);font-family:"Source Sans 3",Arial,sans-serif;color:var(--text);position:relative}
.header-band{position:absolute;left:0;top:0;width:1120px;height:108px;background:linear-gradient(#17993f,#0c8030)}
.brand{position:absolute;left:106px;top:14px;display:flex;align-items:center;gap:14px}
.brand-mark{width:42px;height:42px;border-radius:50%;background:#f2f2f2}
.brand-name{font-size:32px;color:#fff;font-weight:400;letter-spacing:1px}
.search{position:absolute;left:868px;top:22px;width:157px;height:22px;background:#fff;border:1px solid #cfd8cf;font-size:11px;font-style:italic;color:#aaa;padding:3px 10px}
.search svg{position:absolute;right:5px;top:5px}
.page{position:absolute;left:103px;top:88px;width:924px;height:1021px;background:var(--panel);border-radius:4px;box-shadow:0 0 3px rgba(0,0,0,.35)}
.slider{position:absolute;left:16px;top:17px;width:891px;height:301px;border-radius:10px;overflow:hidden;background:linear-gradient(90deg,#eee 0%,#fafafa 60%,#e6e6e6 100%);box-shadow:0 6px 8px rgba(0,0,0,.25)}
.slider-photo{position:absolute;left:0;top:0;width:520px;height:301px;background:linear-gradient(90deg,#b5a48f 0%,#c9a88a 35%,#a7b6c6 65%,rgba(240,240,240,0) 100%)}
.slide-title{position:absolute;left:538px;top:43px;font-size:17px;line-height:30px;color:var(--green-dark)}
.slide-text{position:absolute;left:538px;top:113px;width:320px;font-size:12px;line-height:17px;color:#444}
.btn-read{position:absolute;left:705px;top:183px;width:136px;height:43px;border-radius:3px;background:linear-gradient(#1fa447,#0d7d2f);color:#fff;font-size:17px;text-align:center;line-height:43px;box-shadow:0 3px 4px rgba(0,0,0,.3)}
.arrow{position:absolute;top:138px}
.arrow.prev{left:4px}.arrow.next{right:4px}
.nav{position:absolute;left:16px;top:342px;width:251px;height:317px;background:linear-gradient(90deg,var(--green-light),var(--green-dark));border-radius:3px;padding:8px 2px 0 2px;list-style:none}
.nav li{height:33.6px;border-bottom:1px dotted rgba(255,255,255,.35);color:var(--nav-text);font-size:13px;display:flex;align-items:center;padding-left:18px;gap:12px}
.nav li:last-child{border-bottom:none}
.nav li::before{content:"";width:10px;height:10px;border-radius:50%;background:radial-gradient(circle,#fff 0 20%,#0c6d28 30%)}
.feed{position:absolute;left:16px;top:679px;width:251px;height:317px;border:1px solid #9fb3aa;border-radius:3px;background:linear-gradient(#fff,#c9d6d1);padding:14px 10px 0 10px;font-size:11.5px;line-height:13.5px;color:#333}
.feed-head{display:flex;align-items:center;gap:12px;height:50px;margin-bottom:18px}
.feed-icon{width:44px;height:44px;background:#2a9ad6;border-radius:6px}
.feed-head h3{font-weight:400;font-size:17px;color:#1e4e6b}
.feed-item{margin-bottom:15px}
.feed-time{color:var(--green-dark)}
.feed-more{position:absolute;right:16px;bottom:14px;color:var(--green-dark);font-size:12px}
.blog-head{position:absolute;left:293px;top:346px;width:606px;height:41px;background:#f0f0f0;font-size:22px;color:#333;padding:8px 0 0 24px}
.post{position:absolute;left:293px;width:606px;height:97px}
.post-img{position:absolute;left:0;top:0;width:183px;height:97px;border:2px solid #ccc;border-radius:6px}
.post h4{position:absolute;left:195px;top:2px;width:400px;font-weight:400;font-size:13px;line-height:17px;color:var(--green-text)}
.post p{position:absolute;left:195px;top:43px;width:410px;font-size:11px;line-height:17px;color:#444}
.post .more{position:absolute;right:6px;top:97px;font-size:11px;color:var(--green-text)}
.tags{position:absolute;left:295px;top:827px;width:600px;height:167px;background:#f3f3f3;border:1px solid #ddd;border-radius:3px;padding:22px 20px;font-size:12.2px;line-height:22.4px;color:#555}
.social{position:absolute;left:103px;top:1131px;display:flex;gap:5px}
.social span{width:22px;height:22px;border-radius:2px}
.legal{position:absolute;right:90px;top:1141px;font-size:11px;color:#555;text-align:right;line-height:24px}
.legal .sep{margin:0 10px}
</style>
</head>
<body>
<div class="header-band"></div>
<div class="brand"><span class="brand-mark"></span><span class="brand-name">Wehklang!de</span></div>
<div class="search">Search
  <svg width="10" height="10" viewBox="0 0 10 10"><circle cx="4" cy="4" r="3" fill="none" stroke="#bbb" stroke-width="1.3"/><line x1="6.2" y1="6.2" x2="9.5" y2="9.5" stroke="#bbb" stroke-width="1.5"/></svg>
</div>

<main class="page">
  <section class="slider">
    <div class="slider-photo" role="img" aria-label="Children painting together at a classroom table"></div>
    <div class="slide-title">We are a charity Organization &amp;<br>You can help us in our goal</div>
    <p class="slide-text">Lorem ipsum dolor sit amet, consectetur elit. Lorem ipsum dolor sit amet, consectetur Lorem ipsum dolor sit amet, consectetur elit. Lorem ipsum dolor sit amet, consectetur</p>
    <div class="btn-read">Read More</div>
    <svg class="arrow prev" width="22" height="48" viewBox="0 0 22 48"><polyline points="20,2 3,24 20,46" fill="none" stroke="#8a8a8a" stroke-width="3"/></svg>
    <svg class="arrow next" width="22" height="48" viewBox="0 0 22 48"><polyline points="2,2 19,24 2,46" fill="none" stroke="#8a8a8a" stroke-width="3"/></svg>
  </section>

  <ul class="nav">
    <li>HOME</li><li>ABOUT US</li><li>SERVICES</li><li>HOW WEHKLANG WORKS</li><li>CHARITY MEMBERSHIP</li><li>COMPANY FUNDRASIING</li><li>PARTENERSHIPS</li><li>HELP</li><li>CONTACT US</li>
  </ul>

  <aside class="feed">
    <div class="feed-head"><span class="feed-icon"></span><h3>Chirper Update</h3></div>
    <div class="feed-item">Tomas Reiner<br>Rate limit exceeded. Clients may not make more than 150 requests per hour........<br>Is there a way to over come this limitation?<br><span class="feed-time">1 year 29 weeks ago</span></div>
    <div class="feed-item">Lena Marit Solberg<br>How can I get code from the feed to blog?<br><span class="feed-time">19 weeks 1 day ago</span></div>
    <div class="feed-item">Tomas Reiner<br>Rate limit exceeded. Clients may not make more than 150 requests per hour........<br>Is there a way to over come this limitation?<br><span class="feed-time">1 year 29 weeks ago</span></div>
    <div class="feed-more">MORE &gt;&gt;</div>
  </aside>

  <h2 class="blog-head" style="font-weight:400">OUR BLOG</h2>

  <article class="post" style="top:412px">
    <div class="post-img" role="img" aria-label="Many open hands held together" style="background:linear-gradient(135deg,#7a5a45,#b98d6c,#6b5040)"></div>
    <h4>Uenim ad minim veniam, quis nostrud laborisnisi utaliquip ex ea commodoconsequat.</h4>
    <p>Uenim ad minim veniam, quis nostrud laborisnisi utaliquip ex ea commodoconsequat. Uenim ad minim veniam, quis nostrud laborisnisi utaliquip modoconsequat. ostrud laborisnisi utaliquip ex ea commodoconsequat.</p>
    <span class="more">Readmore</span>
  </article>
  <article class="post" style="top:544px">
    <div class="post-img" role="img" aria-label="Three children holding a give sign" style="background:linear-gradient(90deg,#d9708f,#2e55a8,#3fae5a)"></div>
    <h4>Uenim ad minim veniam, quis nostrud laborisnisi utaliquip ex ea commodoconsequat.</h4>
    <p>Uenim ad minim veniam, quis nostrud laborisnisi utaliquip ex ea commodoconsequat. Uenim ad minim veniam, quis nostrud laborisnisi utaliquip modoconsequat. ostrud laborisnisi utaliquip ex ea commodoconsequat.</p>
    <span class="more">Readmore</span>
  </article>
  <article class="post" style="top:675px">
    <div class="post-img" role="img" aria-label="Linked arms forming a circle" style="background:radial-gradient(circle,#f4f4f4 20%,#e0b59a 60%,#f2f2f2)"></div>
    <h4>Uenim ad minim veniam, quis nostrud laborisnisi utaliquip ex ea commodoconsequat.</h4>
    <p>Uenim ad minim veniam, quis nostrud laborisnisi utaliquip ex ea commodoconsequat. Uenim ad minim veniam, quis nostrud laborisnisi utaliquip modoconsequat. ostrud laborisnisi utaliquip ex ea commodoconsequat.</p>
    <span class="more">Readmore</span>
  </article>

  <div class="tags">Charity,&nbsp; Cancer, Children, Conservation, Disaster Relief, Education, Environment, Family/Parent Support, Health, Homelessness, Human Rights, Hunger, Literacy, Mental Challenges, Miscellaneous, Peace, Physical Challenges, Poverty, Water, Weapons Reduction, Women, Abuse, Adoption, Fostering, Orphans, AIDS &amp; HIV, Animals, At-Risk/Disadvantaged Youths, Cancer, Children, Conservation, Disaster Relief, Education, Environment, Family/Parent Support, Health, Homelessness, Human Rights, Hunger, Literacy,</div>
</main>

<div class="social">
  <span style="background:#3b5a9a"></span><span style="background:#33a9e0"></span><span style="background:#0a73a8"></span><span style="background:#d2392b"></span><span style="background:#8d1a6b"></span>
</div>
<div class="legal">
  Privacy Policy<span class="sep">|</span>Terms &amp; Conditions<span class="sep">|</span>Contact Us<br>
  © 2013 wehklang.de, All Rights Reserved
</div>
</body>
</html>
```